Business Card

Need business cards and small flyers for a musical band

Target Market(s)

Promoters, clients seeking to hire a Latin band

Industry/Entity Type

Business

Requirements
Must have
• The name of the band is Orchestra Brisa so want to have the background with a fire design, with black card and the name of the band in RED, maybe a combination of Red with some yellow. See attached idea.
Nice to have
• See attached files for some ideas.

```html
<!DOCTYPE html>
<html lang="en">
<head>
<meta charset="utf-8">
<title>Orchestra Brisa — Business Card</title>
<link rel="stylesheet" href="https://fonts.googleapis.com/css2?family=Ubuntu:wght@400;500&display=swap">
<style>
  :root {
    --page-bg: #2a2520;
    --card-black: #050302;
    --flame-deep: #7a1a04;
    --flame-red: #d9360c;
    --flame-orange: #f47a14;
    --flame-yellow: #ffd24a;
    --brand-red: #e8461a;
    --contact-orange: #f0601f;
  }
  * { box-sizing: border-box; margin: 0; padding: 0; }
  html, body {
    width: 1200px;
    height: 1000px;
    overflow: hidden;
    background: var(--page-bg);
  }
  .stage {
    width: 1200px;
    height: 1000px;
    display: flex;
    align-items: center;
    justify-content: center;
  }
  .business-card {
    position: relative;
    width: 1000px;
    height: 572px;
    background: var(--card-black);
    border-radius: 6px;
    overflow: hidden;
    box-shadow: 0 20px 50px rgba(0, 0, 0, 0.55);
    font-family: "Ubuntu", "Segoe UI", sans-serif;
  }
  .flame-clef {
    position: absolute;
    left: 40px;
    top: 40px;
    width: 430px;
    height: 420px;
    border-radius: 50%;
    background: radial-gradient(ellipse at 50% 50%,
      var(--flame-yellow) 0%,
      var(--flame-orange) 28%,
      var(--flame-red) 52%,
      var(--flame-deep) 70%,
      rgba(5, 3, 2, 0) 78%);
  }
  .brand-name {
    position: absolute;
    right: 70px;
    top: 120px;
    text-align: right;
    color: var(--brand-red);
    font-weight: 500;
    text-transform: uppercase;
    line-height: 1;
  }
  .brand-name .brand-line-small {
    display: block;
    font-size: 52px;
    letter-spacing: 6px;
  }
  .brand-name .brand-line-large {
    display: block;
    font-size: 148px;
    letter-spacing: 8px;
    margin-top: 6px;
  }
  .contact-line {
    position: absolute;
    left: 0;
    right: 0;
    bottom: 34px;
    text-align: center;
    color: var(--contact-orange);
    font-size: 30px;
    font-weight: 400;
    letter-spacing: 1px;
    white-space: nowrap;
  }
  .contact-line .divider {
    display: inline-block;
    width: 4px;
    height: 30px;
    margin: 0 14px;
    background: var(--flame-red);
    vertical-align: -5px;
  }
</style>
</head>
<body>
  <main class="stage">
    <article class="business-card">
      <div class="flame-clef" role="img" aria-label="Treble clef illustration made of orange and yellow flames"></div>
      <h1 class="brand-name">
        <span class="brand-line-small">Orchestra</span>
        <span class="brand-line-large">Brisa</span>
      </h1>
      <p class="contact-line">
        <span class="contact-name">Rafael Montoya</span><span class="divider"></span><span class="contact-role">Musical Director</span><span class="divider"></span><span class="contact-phone">P: (555) 203 - 7718</span>
      </p>
    </article>
  </main>
</body>
</html>
```